Design bcard for Lumerant Advising and Coaching LLC

I need a logo inspired by the term Lumerant. I'd like to have type of work I do on the back side, i.e. provide C and T on DEIJ, SDOH,...... Front of card--business name, contact information, and possibly a tag line.

Target Market(s)

NGOs, human service agencies, education, healthcare, public health.

Contact Information for Business Card

Name of business, email address, phone number, logo--on front. Services on the back

Font styles to use
Sans Serif

Requirements
Must have
• Contact information, creative logo, services

```html
<!DOCTYPE html>
<html lang="en">
<head>
<meta charset="utf-8">
<title>Lumerant Advising and Coaching LLC – Business Card</title>
<link href="https://fonts.googleapis.com/css2?family=Lato:wght@400;700;900&display=swap" rel="stylesheet">
<style>
  :root {
    --stage: #3a3a3a;
    --green: #4ea24f;
    --green-light: #a9d4a6;
    --white: #ffffff;
    --ink: #4a4a4a;
  }
  html, body {
    margin: 0;
    width: 1200px;
    height: 689px;
    overflow: hidden;
    background: var(--stage);
    font-family: "Lato", sans-serif;
  }
  .stage {
    position: relative;
    width: 1200px;
    height: 689px;
  }
  .card {
    position: absolute;
    top: 190px;
    width: 540px;
    height: 310px;
    border-radius: 16px;
    overflow: hidden;
    box-shadow: 0 18px 40px rgba(0,0,0,.45);
  }
  .card--back { left: 40px; background: var(--green); color: var(--white); }
  .card--front { left: 620px; background: var(--white); color: var(--green); }

  .brand { position: absolute; display: flex; flex-direction: column; }
  .brand__row { display: flex; align-items: center; gap: 10px; }
  .brand__dot { width: 16px; height: 16px; border-radius: 50%; background: currentColor; flex: none; }
  .brand__name { font-weight: 900; letter-spacing: 1px; line-height: 1; }
  .brand__sub { margin-top: 6px; margin-left: 26px; white-space: nowrap; }

  .card--back .brand { left: 60px; top: 92px; }
  .card--back .brand__name { font-size: 64px; }
  .card--back .brand__sub { font-size: 14px; letter-spacing: 5px; }

  .services {
    position: absolute;
    left: 40px; right: 40px; bottom: 34px;
    margin: 0;
    font-size: 12.5px;
    line-height: 1.6;
    text-align: center;
  }

  .card--front .brand { left: 28px; top: 40px; }
  .card--front .brand__row { gap: 8px; }
  .card--front .brand__dot { width: 12px; height: 12px; }
  .card--front .brand__name { font-size: 38px; }
  .card--front .brand__sub { font-size: 9px; letter-spacing: 3px; margin-left: 20px; }

  .person { position: absolute; right: 32px; top: 44px; text-align: right; }
  .person__name { font-size: 22px; font-weight: 900; letter-spacing: 1px; margin: 0; line-height: 1.1; }
  .person__title { font-size: 13px; color: var(--ink); margin: 3px 0 0; }

  .contacts {
    position: absolute; left: 36px; top: 112px;
    list-style: none; margin: 0; padding: 0;
    font-size: 13.5px; color: var(--ink);
  }
  .contacts li { display: flex; align-items: center; gap: 10px; height: 20px; }
  .contacts svg { width: 12px; height: 12px; fill: var(--green); flex: none; }

  .band { position: absolute; inset: 0; width: 540px; height: 310px; }
  .tagline {
    position: absolute; right: 34px; bottom: 26px;
    color: var(--white); font-size: 13px; letter-spacing: 1.5px; margin: 0;
  }
</style>
</head>
<body>
<main class="stage">

  <section class="card card--back" aria-label="Card back">
    <div class="brand">
      <div class="brand__row">
        <span class="brand__dot"></span>
        <span class="brand__name">LUMERANT</span>
      </div>
      <span class="brand__sub">ADVISING AND COACHING LLC</span>
    </div>
    <p class="services">
      Health Care &amp; Quality | Neighborhood &amp; Built Environment | Economic Stability<br>
      Social and Community Context | Education Access and Quality
    </p>
  </section>

  <section class="card card--front" aria-label="Card front">
    <svg class="band" viewBox="0 0 540 310" aria-hidden="true">
      <path d="M0,246 Q330,246 540,96 L540,108 Q330,258 0,258 Z" fill="var(--green-light)"/>
      <path d="M0,264 Q330,264 540,114 L540,310 L0,310 Z" fill="var(--green)"/>
    </svg>

    <div class="brand">
      <div class="brand__row">
        <span class="brand__dot"></span>
        <span class="brand__name">LUMERANT</span>
      </div>
      <span class="brand__sub">ADVISING AND COACHING LLC</span>
    </div>

    <div class="person">
      <p class="person__name">ALEX MORGAN</p>
      <p class="person__title">Founder &amp; CEO</p>
    </div>

    <ul class="contacts">
      <li><svg viewBox="0 0 24 24"><path d="M6.6 10.8a15 15 0 0 0 6.6 6.6l2.2-2.2a1 1 0 0 1 1-.25 11.4 11.4 0 0 0 3.6.57 1 1 0 0 1 1 1V20a1 1 0 0 1-1 1A17 17 0 0 1 3 4a1 1 0 0 1 1-1h3.5a1 1 0 0 1 1 1c0 1.25.2 2.45.57 3.570a1 1 0 0 1-.25 1z"/></svg>(555) 210-4386</li>
      <li><svg viewBox="0 0 24 24"><path d="M7 1h10a2 2 0 0 1 2 2v18a2 2 0 0 1-2 2H7a2 2 0 0 1-2-2V3a2 2 0 0 1 2-2zm0 3v14h10V4zm5 15.5a1 1 0 1 0 0 2 1 1 0 0 0 0-2z"/></svg>(555) 318-7742</li>
      <li><svg viewBox="0 0 24 24"><path d="M6 2h12v6H6zM4 9h16a2 2 0 0 1 2 2v7h-4v4H6v-4H2v-7a2 2 0 0 1 2-2zm4 7v4h8v-4z"/></svg>(555) 427-9150</li>
      <li><svg viewBox="0 0 24 24"><path d="M2 5h20v14H2zm2 2v.5l8 5 8-5V7z"/></svg>info@yourwebsite.com</li>
      <li><svg viewBox="0 0 24 24"><path d="M12 2a10 10 0 1 0 0 20 10 10 0 0 0 0-20zm0 2c1 1.3 1.8 3 2.1 5H9.9C10.2 7 11 5.3 12 4zM4.3 13a8 8 0 0 1 0-2h3.5a16 16 0 0 0 0 2zm5.6 0a14 14 0 0 1 0-2h4.2a14 14 0 0 1 0 2zm6.3 0a16 16 0 0 0 0-2h3.5a8 8 0 0 1 0 2zM12 20c-1-1.3-1.8-3-2.1-5h4.2c-.3 2-1.100 3.7-2.1 5z"/></svg>yourwebsite.com</li>
    </ul>

    <p class="tagline">YOUR TAGLINE GOES HERE</p>
  </section>

</main>
</body>
</html>
```